Food Festival "Signature Cocktail" Booth Banner

Need a 3'x9'6" (36" tall x 114" wide) Outdoor Banner for a new "Signature Cocktail" booth at an outdoor food festival. Marlowe Onion Jubilee is a non profit festival and the World Record largest Garlic Festival with average of 100K attendees over 3 days. Actual drink served will vary from year to year, but banner for the booth with be reused each year so it will be non drink specific. Banner needs to catch attendee's attention both at a quick glance and from a distance outdoors to drive traffic and sales to the booth. It will be mounted above the sales window of a 10x10 Festival Booth on PVC frame (see attached pic for reference). "Signature Cocktail" is required text along with it being identified as a Marlowe Onion Jubilee booth either through use of attached logo (color can be modified) or "Marlowe Onion Jubilee" text since we also have for profit competing vendors. Banner will be full color print. Idea concepts: Neon Sign, Art Deco elegant, reclaimed wood...but open to any concepts. Festival website: https://marloweonionjubilee.example

Target Market(s)

Food Festival Attendees

Font styles to use
Decorative
Script
Other font styles liked:
• Neon, heavy weight fonts, open.

Colors

Designer to choose colors to be used in the design.

Requirements
Must have
• "Signature Cocktail" and "Marlowe Onion Jubilee" text or MOJ Logo provided, colors and layout that stands out and easily identifiable and readable from a long distance with strong text
Nice to have
• Vibrant engaging background,, ties to Garlic
Should not have
• Clip art, generic text

```html
<!DOCTYPE html>
<html lang="en">
<head>
<meta charset="utf-8">
<title>Signature Cocktail Booth Banner</title>
<link rel="stylesheet" href="https://fonts.googleapis.com/css2?family=Anton&family=Montserrat:wght@500&display=swap">
<style>
  :root {
    --backdrop: #4d4d4d;
    --lime: #8cc84b;
    --lime-line: #7fb842;
    --divider: #3e7a2a;
    --magenta: #b33a9c;
    --magenta-dark: #8f2a7c;
    --navy: #262f68;
    --white: #ffffff;
    --photo-warm: #c98a4f;
    --photo-green: #6f8a4c;
    --photo-crowd: #7d8a5a;
  }
  html, body {
    margin: 0;
    width: 1200px;
    height: 1200px;
    overflow: hidden;
    background: var(--backdrop);
  }
  .canvas {
    position: relative;
    width: 1200px;
    height: 1200px;
  }
  .banner {
    position: absolute;
    left: 50px;
    top: 426px;
    width: 1100px;
    height: 347px;
    box-shadow: 0 2px 6px rgba(0,0,0,.35);
  }
  .banner svg { display: block; width: 100%; height: 100%; }
  .title { font-family: "Anton", "Impact", sans-serif; fill: var(--white); }
  .ribbon-text { font-family: "Anton", "Impact", sans-serif; fill: var(--white); }
  .date-text { font-family: "Montserrat", "Arial", sans-serif; font-weight: 500; fill: var(--white); }
</style>
</head>
<body>
<main class="canvas">
  <section class="banner" aria-label="Signature Cocktail booth banner">
    <svg viewBox="0 0 1020 322" xmlns="http://www.w3.org/2000/svg">
      <defs>
        <linearGradient id="photo-top" x1="0" y1="0" x2="1" y2="1">
          <stop offset="0" stop-color="#5e6b4a"/>
          <stop offset="1" stop-color="#c07a6a"/>
        </linearGradient>
        <linearGradient id="photo-left" x1="0" y1="0" x2="1" y2="1">
          <stop offset="0" stop-color="#5a5f4c"/>
          <stop offset="1" stop-color="#d98a3a"/>
        </linearGradient>
        <linearGradient id="photo-bottom" x1="0" y1="0" x2="1" y2="1">
          <stop offset="0" stop-color="#6d8a52"/>
          <stop offset="1" stop-color="#c9b9a0"/>
        </linearGradient>
      </defs>

      <!-- field -->
      <rect class="field" x="0" y="0" width="1020" height="322" fill="var(--lime)"/>

      <!-- photo collage -->
      <g class="photo-collage">
        <polygon role="img" aria-label="Photo of festival guests sharing a drink" points="0,0 320,0 180,161 0,0" fill="url(#photo-top)"/>
        <polygon role="img" aria-label="Photo of colourful grilled food being served" points="0,0 180,161 0,322" fill="url(#photo-left)"/>
        <polygon role="img" aria-label="Photo of festival crowd on the grounds" points="0,322 180,161 320,322" fill="url(#photo-bottom)"/>
        <g stroke="var(--divider)" stroke-width="4">
          <line x1="6" y1="0" x2="180" y2="161"/>
          <line x1="180" y1="161" x2="6" y2="322"/>
        </g>
        <polyline points="320,0 180,161 320,322" fill="none" stroke="var(--lime)" stroke-width="3"/>
      </g>

      <!-- headline -->
      <text class="title" x="645" y="94" text-anchor="middle" font-size="88" textLength="620" lengthAdjust="spacingAndGlyphs">Signature Cocktail</text>

      <!-- ribbon -->
      <g class="ribbon">
        <polygon points="325,118 440,118 440,196 325,196 350,157" fill="var(--magenta)"/>
        <polygon points="985,118 870,118 870,196 985,196 960,157" fill="var(--magenta)"/>
        <polygon points="418,196 440,196 440,214" fill="var(--magenta-dark)"/>
        <polygon points="892,196 870,196 870,214" fill="var(--magenta-dark)"/>
        <rect x="418" y="126" width="474" height="88" fill="var(--magenta)"/>
        <text class="ribbon-text" x="655" y="194" text-anchor="middle" font-size="48" textLength="415" lengthAdjust="spacingAndGlyphs">Marlowe Onion Jubilee</text>
      </g>

      <!-- dates -->
      <g class="dates">
        <rect x="451" y="246" width="425" height="40" rx="20" fill="var(--navy)"/>
        <text class="date-text" x="663" y="277" text-anchor="middle" font-size="32">July 27, 28 and 29</text>
      </g>
    </svg>
  </section>
</main>
</body>
</html>
```